Fiber artist in need of animated text design for tag line

In need of animated text letter design for a fiber artists tag line ,
"All Fabric No Paint". The artist is of African descent and the text should reflect vibrance and be colorful . The text should be consistent but
"All Fabric" can be a brighter color or pattern similar to African or ethnic textiles while "No Paint" can be slightly less colorful or appear to be textured paint strokes. My idea for the text would be similar to commercial advertisement lettering on products found in a market with some type of a border effect around the primary lettering.

```html
<!DOCTYPE html>
<html lang="en">
<head>
<meta charset="utf-8">
<title>All Fabric No Paint – Tagline Variations</title>
<link rel="stylesheet" href="https://fonts.googleapis.com/css2?family=Oswald:wght@600&family=Varela+Round&display=swap">
<style>
  :root {
    --page: #ffffff;
    --band-orange: #f18e20;
    --band-red: #a21e23;
    --stitch: #ffffff;
    --paint-navy: #243570;
    --paint-blue: #0875b8;
    --fabric-green: #5db946;
    --fabric-orange: #f07423;
    --fabric-navy: #232a6b;
    --fabric-peach: #fbc9a4;
    --ink: #ffffff;
  }
  * { margin: 0; padding: 0; box-sizing: border-box; }
  html, body { width: 1200px; height: 735px; overflow: hidden; background: var(--page); }
  .sheet { position: relative; width: 1200px; height: 735px; }
  .tag-card { position: absolute; width: 458px; height: 307px; display: block; }
  .tag-card--a { left: 101px; top: 27px; }
  .tag-card--b { left: 636px; top: 26px; }
  .tag-card--c { left: 104px; top: 399px; }
  .tag-card--d { left: 639px; top: 399px; }
  .fabric-word {
    font-family: "Varela Round", sans-serif;
    font-size: 146px;
    fill: none;
    stroke: var(--stitch);
    stroke-width: 2.2;
  }
  .paint-word {
    font-family: "Oswald", sans-serif;
    font-weight: 600;
    font-size: 126px;
    fill: var(--ink);
  }
  .stitch-line { stroke: var(--stitch); stroke-width: 4; stroke-dasharray: 22 14; fill: none; }
  .frame-line { fill: none; stroke: var(--ink); stroke-width: 2; }
</style>
</head>
<body>
<main class="sheet">

  <svg class="tag-card tag-card--a" viewBox="0 0 826 555" preserveAspectRatio="none">
    <defs>
      <linearGradient id="paintA" x1="0" y1="0" x2="1" y2="1">
        <stop offset="0" stop-color="var(--paint-navy)"/>
        <stop offset="0.45" stop-color="var(--paint-blue)"/>
        <stop offset="1" stop-color="var(--paint-navy)"/>
      </linearGradient>
      <linearGradient id="fabricA" x1="0" y1="0" x2="1" y2="1">
        <stop offset="0" stop-color="var(--fabric-navy)"/>
        <stop offset="0.35" stop-color="var(--fabric-green)"/>
        <stop offset="0.65" stop-color="var(--fabric-orange)"/>
        <stop offset="1" stop-color="var(--fabric-green)"/>
      </linearGradient>
    </defs>
    <rect class="paint-field" width="826" height="555" fill="url(#paintA)" role="img" aria-label="Blue paint brush-stroke texture"/>
    <polygon class="fabric-field" points="0,0 826,0 826,80 0,248" fill="url(#fabricA)" role="img" aria-label="African wax-print textile pattern of green and navy medallions on orange"/>
    <polygon class="band-red" points="0,422 826,260 826,278 0,442" fill="var(--band-red)"/>
    <polygon class="band-orange" points="0,248 826,80 826,260 0,422" fill="var(--band-orange)"/>
    <line class="stitch-line" x1="0" y1="266" x2="826" y2="98"/>
    <line class="stitch-line" x1="0" y1="404" x2="826" y2="242"/>
    <text class="fabric-word" transform="translate(36 382) rotate(-11.5)" textLength="758" lengthAdjust="spacingAndGlyphs">ALL FABRIC</text>
    <rect class="frame-line" x="222" y="418" width="514" height="119"/>
    <rect class="frame-line" x="229" y="425" width="500" height="105"/>
    <text class="paint-word" x="479" y="522" text-anchor="middle" textLength="484" lengthAdjust="spacingAndGlyphs">NO PAINT</text>
  </svg>

  <svg class="tag-card tag-card--b" viewBox="0 0 829 557" preserveAspectRatio="none">
    <defs>
      <linearGradient id="paintB" x1="0" y1="0" x2="1" y2="1">
        <stop offset="0" stop-color="var(--paint-navy)"/>
        <stop offset="0.45" stop-color="var(--paint-blue)"/>
        <stop offset="1" stop-color="var(--paint-navy)"/>
      </linearGradient>
      <linearGradient id="fabricB" x1="0" y1="0" x2="1" y2="1">
        <stop offset="0" stop-color="var(--fabric-green)"/>
        <stop offset="0.4" stop-color="var(--fabric-peach)"/>
        <stop offset="0.7" stop-color="var(--fabric-navy)"/>
        <stop offset="1" stop-color="var(--fabric-green)"/>
      </linearGradient>
    </defs>
    <rect class="paint-field" width="829" height="557" fill="url(#paintB)" role="img" aria-label="Blue paint brush-stroke texture"/>
    <polygon class="fabric-field" points="0,0 829,0 829,35 0,200" fill="url(#fabricB)" role="img" aria-label="African wax-print textile pattern of large green and navy medallions on peach"/>
    <polygon class="band-red" points="0,378 829,215 829,262 0,428" fill="var(--band-red)"/>
    <polygon class="band-orange" points="0,200 829,35 829,215 0,378" fill="var(--band-orange)"/>
    <line class="stitch-line" x1="0" y1="218" x2="829" y2="53"/>
    <line class="stitch-line" x1="0" y1="360" x2="829" y2="197"/>
    <text class="fabric-word" transform="translate(38 340) rotate(-11.3)" textLength="758" lengthAdjust="spacingAndGlyphs">ALL FABRIC</text>
    <rect class="frame-line" x="224" y="410" width="512" height="118"/>
    <rect class="frame-line" x="231" y="417" width="498" height="104"/>
    <text class="paint-word" x="480" y="513" text-anchor="middle" textLength="484" lengthAdjust="spacingAndGlyphs">NO PAINT</text>
  </svg>

  <svg class="tag-card tag-card--c" viewBox="0 0 826 555" preserveAspectRatio="none">
    <defs>
      <linearGradient id="paintC" x1="0" y1="0" x2="1" y2="1">
        <stop offset="0" stop-color="var(--paint-navy)"/>
        <stop offset="0.45" stop-color="var(--paint-blue)"/>
        <stop offset="1" stop-color="var(--paint-navy)"/>
      </linearGradient>
      <linearGradient id="fabricC" x1="0" y1="0" x2="1" y2="1">
        <stop offset="0" stop-color="var(--fabric-navy)"/>
        <stop offset="0.4" stop-color="var(--fabric-orange)"/>
        <stop offset="0.7" stop-color="var(--fabric-green)"/>
        <stop offset="1" stop-color="var(--fabric-navy)"/>
      </linearGradient>
    </defs>
    <rect class="paint-field" width="826" height="555" fill="url(#paintC)" role="img" aria-label="Blue paint brush-stroke texture"/>
    <polygon class="fabric-field" points="0,0 826,0 826,80 0,248" fill="url(#fabricC)" role="img" aria-label="African wax-print textile pattern of large green and navy medallions on orange"/>
    <polygon class="band-red" points="0,422 826,260 826,278 0,442" fill="var(--band-red)"/>
    <polygon class="band-orange" points="0,248 826,80 826,260 0,422" fill="var(--band-orange)"/>
    <line class="stitch-line" x1="0" y1="266" x2="826" y2="98"/>
    <line class="stitch-line" x1="0" y1="404" x2="826" y2="242"/>
    <text class="fabric-word" transform="translate(36 382) rotate(-11.5)" textLength="758" lengthAdjust="spacingAndGlyphs">ALL FABRIC</text>
    <rect class="frame-line" x="222" y="418" width="514" height="119"/>
    <rect class="frame-line" x="229" y="425" width="500" height="105"/>
    <text class="paint-word" x="479" y="522" text-anchor="middle" textLength="484" lengthAdjust="spacingAndGlyphs">NO PAINT</text>
  </svg>

  <svg class="tag-card tag-card--d" viewBox="0 0 829 557" preserveAspectRatio="none">
    <defs>
      <linearGradient id="paintD" x1="0" y1="0" x2="1" y2="1">
        <stop offset="0" stop-color="var(--paint-navy)"/>
        <stop offset="0.45" stop-color="var(--paint-blue)"/>
        <stop offset="1" stop-color="var(--paint-navy)"/>
      </linearGradient>
      <linearGradient id="fabricD" x1="0" y1="0" x2="1" y2="1">
        <stop offset="0" stop-color="var(--fabric-orange)"/>
        <stop offset="0.4" stop-color="var(--fabric-green)"/>
        <stop offset="0.7" stop-color="var(--fabric-navy)"/>
        <stop offset="1" stop-color="var(--fabric-peach)"/>
      </linearGradient>
    </defs>
    <rect class="paint-field" width="829" height="557" fill="url(#paintD)" role="img" aria-label="Blue paint brush-stroke texture"/>
    <polygon class="fabric-field" points="0,0 829,0 829,35 0,200" fill="url(#fabricD)" role="img" aria-label="African wax-print textile pattern of green and navy medallions on orange"/>
    <polygon class="band-red" points="0,378 829,215 829,262 0,428" fill="var(--band-red)"/>
    <polygon class="band-orange" points="0,200 829,35 829,215 0,378" fill="var(--band-orange)"/>
    <line class="stitch-line" x1="0" y1="218" x2="829" y2="53"/>
    <line class="stitch-line" x1="0" y1="360" x2="829" y2="197"/>
    <text class="fabric-word" transform="translate(38 340) rotate(-11.3)" textLength="758" lengthAdjust="spacingAndGlyphs">ALL FABRIC</text>
    <rect class="frame-line" x="224" y="410" width="512" height="118"/>
    <rect class="frame-line" x="231" y="417" width="498" height="104"/>
    <text class="paint-word" x="480" y="513" text-anchor="middle" textLength="484" lengthAdjust="spacingAndGlyphs">NO PAINT</text>
  </svg>

</main>
</body>
</html>
```